Banner for my Fitness ClipStream channel Peak Forged

I need a Banner to be hung in a gym for my fitness ClipStream Channel called Peak Forged. I was thinking of going with something minmalistic like a ClipStream play button and the name of my ClipStream Channel next to it.
(ClipStream Play Button) | PEAK FORGED
I also would like to add my motto in this banner which is " STRENGTH . PERFORMANCE . LONGEVITY. "
I would like the emphasis to be on youtube play button and the Peak Forged part.
I want something simple but effective that stands out. I will attach a picture of where the banner will be posted so you have a better idea.
My website is www.peakforged.ca
My ClipStream Channel is www.youtube.com/peakforged
I will attach the location of where the banner will go along with my logo
The size of the banner will be 30 inches in height and 80 inches in length
I am attaching some of my pictures that you may be able to incorporate as a faded background picture . You can either use one or all of them, which ever you feel is best

```html
<!DOCTYPE html>
<html lang="en">
<head>
<meta charset="UTF-8">
<title>Peak Forged — Channel Banner</title>
<link rel="stylesheet" href="https://fonts.googleapis.com/css2?family=Montserrat:wght@700;800&family=Roboto:wght@400;700&display=swap">
<style>
  :root {
    --ink-black: #070606;
    --deep-maroon: #2a0404;
    --blood-red: #6e0808;
    --signal-red: #a30d0d;
    --brand-red: #e0302a;
    --text-white: #ffffff;
    --text-soft: #f2eaea;
  }
  html, body {
    margin: 0;
    padding: 0;
    width: 1200px;
    height: 375px;
    overflow: hidden;
    background: var(--ink-black);
  }
  .banner {
    position: relative;
    width: 1200px;
    height: 375px;
    overflow: hidden;
    background: linear-gradient(90deg, var(--ink-black) 0%, var(--deep-maroon) 38%, var(--blood-red) 78%, var(--signal-red) 100%);
  }
  .athlete-photo {
    position: absolute;
    left: 60px;
    top: 0;
    width: 1040px;
    height: 375px;
    background:
      radial-gradient(ellipse 170px 260px at 520px 230px, rgba(190, 20, 20, 0.55), rgba(120, 10, 10, 0) 100%),
      radial-gradient(ellipse 460px 90px at 520px 250px, rgba(160, 15, 15, 0.35), rgba(120, 10, 10, 0) 100%);
  }
  .channel-mark {
    position: absolute;
    left: 65px;
    top: 126px;
    width: 177px;
    display: flex;
    flex-direction: column;
    align-items: center;
    gap: 12px;
  }
  .channel-mark__square {
    width: 84px;
    height: 84px;
    background: var(--brand-red);
  }
  .channel-mark__name {
    font-family: "Montserrat", sans-serif;
    font-weight: 800;
    font-size: 29px;
    color: var(--text-white);
    line-height: 1;
    white-space: nowrap;
  }
  .divider {
    position: absolute;
    left: 315px;
    top: 117px;
    width: 6px;
    height: 148px;
    background: var(--text-white);
  }
  .channel-title {
    position: absolute;
    left: 393px;
    top: 143px;
    margin: 0;
    font-family: "Montserrat", sans-serif;
    font-weight: 800;
    font-size: 86px;
    line-height: 1;
    letter-spacing: 4px;
    color: var(--text-white);
    white-space: nowrap;
  }
  .motto {
    position: absolute;
    left: 331px;
    top: 297px;
    margin: 0;
    font-family: "Roboto", sans-serif;
    font-weight: 700;
    font-size: 21px;
    line-height: 1;
    letter-spacing: 4px;
    color: var(--text-soft);
    white-space: nowrap;
  }
  .website {
    position: absolute;
    left: 505px;
    top: 327px;
    margin: 0;
    font-family: "Roboto", sans-serif;
    font-weight: 400;
    font-size: 21px;
    line-height: 1;
    color: var(--text-soft);
    white-space: nowrap;
  }
</style>
</head>
<body>
  <div class="banner">
    <div class="athlete-photo" role="img" aria-label="Faded red-toned photo of the channel host training shirtless with cable handles, arms spread wide"></div>

    <div class="channel-mark">
      <span class="channel-mark__square"></span>
      <span class="channel-mark__name">ClipStream</span>
    </div>

    <div class="divider"></div>

    <h1 class="channel-title">PEAK FORGED</h1>

    <p class="motto">STRENGTH. PERFORMANCE. LONGEVITY.</p>
    <p class="website">www.peakforged.ca</p>
  </div>
</body>
</html>
```